Catastrophe & Disaster Mitigation & Repairs

1. Fire/smoke & flood/water & wind damage restoration for residential, commercial or industrial structure &/or content.

2. 24/7 emergency service

3. Flood, catastrophe & storm emergency response

4. Emergency board ups.

5. Specializing in insurance claims with direct insurance billing (when applicable).

6. Full service restoration. We handle everything from cleaning & deoderization of content & structure, demo, drying, disposal & dry cleaning to temporary storage, emergency electrical & plumbing & FULL repairs "To Restore residential or commercial property & content to pre loss condition".

7. Please see our website, brochure or simply ask any of our technicians for complete list of services & specialized services that we provide.

However within 60 to 90 days after we incorporate & launch this new business we are starting a sister company that will handle all of the carpentry & construction on all of our insurance jobs as well as market for additional roofing, siding, interiors, exterior, kitchens, baths, additions, painting, insulation, drywall, doors, windows, decks, additions, garages, general contracting, electrical, hardwood floor restoration & instalation, custom tile, vinyl, carpet & laminate flooring installation, tree houses, small concrete repairs, brick repair, doors, windows, new builds, etc, etc. When the time comes I will need business card, rak cards, note books, stickers, yard signs, vehicle magnets, etc for that business (Granite Ridge Building Services) too. So please keep in mind that we can temporarily have construction & full repairs on this card but in the near future the majority of anything carpentry or construction related (aside from demo) will need to be easily removes from this card and replaced with a brief line referring to the sister company.

We have a long long long list of services that we provide for residential, commercial & industrial. Duct cleaning & sanitize, foreclosure clean out, pre & post rental or sale cleaning &/or repairs & painting, home & office cleaning services, post construction clean up, crime scene remediation, smoke & odor removal & mitigation, residential cleaning, commercial cleaning, water proofing, biohazard clean up, septic back up clean up, temporary power, temporary heat, temporary storage, temporary repairs, refrigerant & desiccant & heat drying, mold mitigation (we don't like mold & don't advertise for mold but are educated, trained & equipped to do it upon request or nessecity), full pack out of content, full move back, demo & disposal, indoor air quality testing, consulting, claim negotiation with insurance carrier, content cleaning & restoration, jewelry cleaning, dry cleaning, pressure washing, steam pressure washing, sand & dry ice blasting, graffiti removal, inventory of damaged, destroyed & cleaned content, upholstery & carpet cleaning, grout cleaning, property winterizing, soda blasting, art & document restoration, emergency & long term utility reactivate,
landscaping & clean up of property/yard damaged as result of catastrophe (if covered in policy or upon request), wind or catastorphe damaged tree cut up & removal, project management or consulting, some equipment rental, pump outs, water extraction, electronics cleaning, bat guanno removal & mitigation, mitigation & remediation planning, detailed & itemized written estimates with industry standard pricing software, spring cleaning, hordar clean outs, garage/attic/basement & barn clean out & hauloff, RV clean out, full demo & removal of total loss or condemned structures, no intrest payment plans for the unfortunate & uninsured (with sizeable down payment). I know there are more services that I'm not thinking of too.

When a less than once in a lifetime castorphe strikes a home, business, commercial or industrial structure & often times the content of that structure the owners are often in shock & don't know what direction to turn or where to begin simply because they most likely have never been through a loss of that magnitude & in very unfamiliar territory. The amount of planning, equipment, training, networking, resources, subcontractors, manpower, financing & paperwork can be mindboggling. Especially when the majority of them have jobs, school, family & lives that don't stop due to their misfortune. Crestwell Water & Blaze Recovery LLC handles every aspect from before the time first responders or plumbers are gone until the structure & content is restored to (or better than) preloss condition. They only thing we need from our customers is for them to provide us with material kind & color such as paint & flooring. Aside from that, our customers can go on with there lives and have as little stress & worry as possible given the circumstances. From a small over flowed sink to a large warehouse fire that sets of a high pressure sprinkler system to a structure that's been completely sumburged for several days it is still uncommon territory & still requires a lot of different skilled subcontractors, specialized equipment & logistics. Its what we do every day & we have it well planned in advance, a core team of dedicated & trusted professionals that we've been colleges & friends with for years. The homeowners are still our direct customer & are consulted on every aspect of mitigation & repairs to their home, property &/or content. Our customers are free to choose what (if any) aspects of the project they handle themselves. From time to time they choose to paint their own bedroom or have a friend or family member that's a electrician, plumber or tradesman & chose to use them for that portion of their loss. Point being that even though we can handle every aspect we still work closely with our customers & even if direct insurance invoicing the policy holder/home or structure owner is still our valued customer. We also do as much as we can to get their lives back to as fully functional as possible given the circumstance.

As I'm sure you can tell.... I've provided a lot of text. Please save some for the rack cards, brochures, folders and anything else you may be able to use it in. I have a ton more of informational text from our old website. I also have a lot of testimonials, photos & anything else you may be able to implement in our promotional & informative campaign. We've been in this business for 8 years, in the flood & fire restoration business for 11 years as well as having well over 100 years combined experience in the carpentry & constructive fields. At some point & on something I'd like all our services listed. Maybe on brochures. I attached the brochure that my cousin (who at the time was graphics editor at Pelvora Journal) designed when we first got in business. Its a quality job but I feel is very outdated & not very informative.
I understand that I have just a few seconds to catch my potential customers eye so I feel with the business cards that one side needs to POP, be clean, look good and stand out at you and the other side can list some of our services. I think that #'s 1 thru 7 at the top of this section should be most of it for the back of the business card. Please look through this not so brief, brief & see what you think. I'm gearing towards fire, smoke, flood & wind mitigation. Then cleaning + emergency, storm & catastrophe response.
The biggest thing is that it needs to make both of my competitors attached cards look like shit & unfortunately I kinda like both of their cards so you have your work cut out for you. One of the reasons I gave you such extensive information. Please keep rack cards, brochures, letter heads, envelopes, notebooks, folders, informative literature, documents, stickers, door magnets & everything else we may need for both this & construction business. I'll be able to pay for that next week. I also keep clicking on Double Sided & it keeps changing back to single by itself.

PLEASE NOTE THAT I SUBMITTED FOR "BUSINESS CARD DESIGN" THERE WASNT A OPTION FOR EXACTLY WHAT I NEED HELP WITH. I NEED MY EXISTING LOGO MODIFIED ALONG WITH THE BUSINESS CARD DESIGN. I ALSO NEED A BROCHURE & RACK CARD DESIGNED. I'D LIKE TO DO ALL OF THIS ASAP. PLEASE LET ME KNOW THE CHARGES FOR THESE ADDITIONAL SERVICES. THANK YOU.

Target Market(s)

Insurance agents, insurance adjusters, homeowners/policy holders that have experienced a fire, flood or other catastorphies, plumbers, builders, etc

Industry/Entity Type

Office Cleaning

Contact Information for Business Card

Rick Fansome
Crestwell Water & Blaze Recovery LLC
5183 Tillcorn Rd
Mayville, NY 14757
www.crestwellrecovery-example.com
rick@crestwellrecovery-example.com
Office: 716.555.0142
Cell: 716.555.0187

Requirements
Must have
• I've attached a copy of our old business & logo as well as a old business card. I'd like to incorporate our old logo & colors. Or at least entertain using them in some aspect. Feel free to change it up though. Our old logo is supposed to represent a roof & the red for fire & blue for water.

My old card is cluttered & doesn't catch the eye.

The other cards I've attached are Clearbay Spore Care who is my old business partner from years ago & Hollowmere Renewal is my ex fiance so my new cards don't just need to catch the eye & be functional they need to look at least twice as good as my competitors.
Nice to have
• One side business name, my name, logo, phone #'s, email, website, fb, twitter, instagram, etc. I feel one side should be clean, bold & catch the eye in the 6 seconds I have to do so.

Then opposing side should have some of our more prominent services along with more information.

I'd like to keep away from having the business cards on white card stock. I think a color or multi color looks better.

I guess I'm open to anything. You guys are the pro's. As long as it looks great & gets the point across. I have 2 other people that need the same cards too. Just different names, emails & cell #'s. And as I stated earlier. I'm planning on ordering notepads, yard signs, rack cards, brochures, magnets & a few other things at the same time. I'll need design & layout on all of those too. Just let me know what the additional cost will be. They'll have the same colors, logo & business name. Just more or less info depending on the product.
Should not have
• ?

```html
<!DOCTYPE html>
<html lang="en">
<head>
<meta charset="utf-8">
<title>Crestwell Water &amp; Blaze Recovery – Business Card</title>
<link rel="stylesheet" href="https://fonts.googleapis.com/css2?family=Lobster&family=Cinzel:wght@700;900&family=Arimo:wght@400;700&family=Roboto+Condensed:wght@400;700&display=swap">
<style>
  :root {
    --brand-blue: #1a8fcf;
    --panel-light: #ffffff;
    --panel-edge: #cfd0d2;
    --tile-frame: #c9cbce;
    --tile-dark: #0d0d0f;
    --water: #2f8de0;
    --fire: #d4220f;
    --wind: #c3141c;
    --smoke: #b0101a;
    --mark-grey: #b9bcc0;
  }
  * { box-sizing: border-box; margin: 0; padding: 0; }
  html, body { width: 1050px; height: 1200px; overflow: hidden; background: #fff; }
  .card { position: relative; width: 1050px; height: 1200px; font-family: "Arimo", Arial, sans-serif; }

  .front {
    position: absolute; left: 0; top: 0; width: 1050px; height: 600px;
    background: radial-gradient(ellipse 70% 80% at 50% 45%, var(--panel-light) 0%, #eeeeef 45%, var(--panel-edge) 100%);
  }
  .brand-mark {
    position: absolute; left: 470px; top: 90px; width: 110px; height: 110px;
    border-radius: 50%; background: var(--mark-grey);
  }
  .brand-name {
    position: absolute; left: 0; right: 0; top: 282px; text-align: center;
    font-family: "Lobster", cursive; font-weight: 400; font-size: 46px; color: var(--brand-blue); white-space: nowrap;
  }
  .service-tiles { position: absolute; top: 403px; left: 0; width: 100%; }
  .tile {
    position: absolute; width: 102px; height: 114px; border-radius: 14px;
    background: linear-gradient(180deg, #f4f4f5, var(--tile-frame));
    padding: 6px; box-shadow: 0 2px 4px rgba(0,0,0,.25);
  }
  .tile-face {
    position: relative; width: 100%; height: 100%; border-radius: 9px; overflow: hidden;
    background: linear-gradient(180deg, var(--tile-dark) 0%, var(--tile-dark) 45%, var(--accent) 100%);
  }
  .tile-icon {
    position: absolute; left: 50%; top: 12px; transform: translateX(-50%);
    width: 46px; height: 52px;
  }
  .tile-label {
    position: absolute; left: 0; right: 0; bottom: 8px; text-align: center;
    color: #fff; font-size: 22px;
  }
  .tile-smoke .tile-label { font-weight: 700; }
  .tile-reflection {
    position: absolute; top: 120px; width: 102px; height: 52px; border-radius: 10px 10px 0 0;
    background: linear-gradient(180deg, rgba(160,160,165,.35), rgba(255,255,255,0));
  }
  .tile-reflection span {
    display: block; text-align: center; transform: scaleY(-1); margin-top: 6px;
    font-size: 22px; color: rgba(120,120,130,.35);
  }

  .back { position: absolute; left: 0; top: 600px; width: 1050px; height: 600px; background: #fff; }
  .emergency { position: absolute; left: 30px; top: 30px; width: 210px; text-align: center; color: var(--brand-blue); font-family: "Lobster", cursive; }
  .emergency .hours { font-size: 50px; line-height: 56px; }
  .emergency .line { font-size: 21px; line-height: 28px; white-space: nowrap; }
  .back-title {
    position: absolute; right: 38px; top: 66px; font-family: "Lobster", cursive; font-weight: 400;
    font-size: 42px; color: var(--brand-blue); white-space: nowrap;
  }
  .person-name {
    position: absolute; left: 0; right: 0; top: 270px; text-align: center;
    font-family: "Cinzel", serif; font-weight: 900; font-size: 52px; color: var(--brand-blue); letter-spacing: 1px;
  }
  .services {
    position: absolute; left: 46px; top: 416px; width: 532px;
    font-family: "Roboto Condensed", "Arial Narrow", sans-serif;
    font-size: 21px; font-weight: 700; line-height: 36.5px; color: var(--brand-blue);
    text-align: justify; text-align-last: left;
  }
  .contact {
    position: absolute; left: 668px; top: 416px; width: 372px; color: var(--brand-blue);
    font-family: "Roboto Condensed", "Arial Narrow", sans-serif; font-size: 17px; line-height: 20px;
  }
  .contact-row { position: relative; padding-left: 64px; margin-bottom: 10px; }
  .contact-row svg { position: absolute; left: 0; top: 4px; }
  .contact-row.address { font-size: 16px; }
</style>
</head>
<body>
<div class="card">

  <section class="front">
    <div class="brand-mark" aria-hidden="true"></div>
    <h1 class="brand-name">Crestwell Water &amp; Blaze Recovery</h1>

    <div class="service-tiles">
      <div class="tile tile-water" style="left:210px; --accent: var(--water);">
        <div class="tile-face">
          <svg class="tile-icon" viewBox="0 0 46 52" aria-hidden="true">
            <defs><linearGradient id="drop" x1="0" y1="0" x2="0" y2="1"><stop offset="0" stop-color="#8fd0ff"/><stop offset="1" stop-color="#2a7fd6"/></linearGradient></defs>
            <path d="M23 4 C30 18 36 26 36 34 A13 13 0 0 1 10 34 C10 26 16 18 23 4 Z" fill="url(#drop)"/>
          </svg>
          <span class="tile-label">Water</span>
        </div>
      </div>
      <div class="tile-reflection" style="left:210px;"><span>Water</span></div>

      <div class="tile tile-fire" style="left:386px; --accent: var(--fire);">
        <div class="tile-face">
          <div class="tile-icon" role="img" aria-label="Flame illustration" style="border-radius:40% 40% 30% 30%; background: radial-gradient(ellipse at 50% 70%, #ffd34d, #f08a1c 60%, rgba(240,138,28,0) 75%);"></div>
          <span class="tile-label">Fire</span>
        </div>
      </div>
      <div class="tile-reflection" style="left:386px;"><span>Fire</span></div>

      <div class="tile tile-wind" style="left:566px; --accent: var(--wind);">
        <div class="tile-face">
          <div class="tile-icon" role="img" aria-label="Storm spiral symbol" style="border-radius:50%; background: radial-gradient(circle, rgba(0,0,0,0) 30%, #d2232a 34%, #d2232a 52%, rgba(0,0,0,0) 56%);"></div>
          <span class="tile-label">Wind</span>
        </div>
      </div>
      <div class="tile-reflection" style="left:566px;"><span>Wind</span></div>

      <div class="tile tile-smoke" style="left:736px; --accent: var(--smoke);">
        <div class="tile-face">
          <div class="tile-icon" role="img" aria-label="Smoke cloud image" style="width:70px; height:58px; top:4px; border-radius:50%; background: radial-gradient(ellipse, #e4e4e4 0%, #9a9a9a 55%, rgba(80,80,80,0) 75%);"></div>
          <span class="tile-label">Smoke</span>
        </div>
      </div>
      <div class="tile-reflection" style="left:736px;"><span>Smoke</span></div>
    </div>
  </section>

  <section class="back">
    <div class="emergency">
      <div class="hours">24/7</div>
      <div class="line">Emergency service</div>
      <div class="line">Emergency board ups.</div>
    </div>

    <h2 class="back-title">Crestwell Water &amp; Blaze Recovery</h2>

    <p class="person-name">RICK FANSOME</p>

    <p class="services">Fire/smoke &amp; flood/water &amp; wind damage restoration for residential, commercial or industrial structure &amp;/or content. Specializing in insurance claims with direct insurance billing (when applicable).</p>

    <div class="contact">
      <div class="contact-row">
        <svg width="34" height="34" viewBox="0 0 34 34" aria-hidden="true">
          <circle cx="17" cy="17" r="15" fill="none" stroke="var(--brand-blue)" stroke-width="1.6"/>
          <path d="M12 9 l3 4 -2 2 c1 3 3 5 6 6 l2-2 4 3 -2 3 c-7 0-13-6-13-13 z" fill="none" stroke="var(--brand-blue)" stroke-width="1.4" stroke-linejoin="round"/>
        </svg>
        Cell &nbsp;&nbsp;: 555-555-0187<br>Office: 555-555-0142
      </div>
      <div class="contact-row address">
        <svg width="36" height="30" viewBox="0 0 36 30" aria-hidden="true">
          <path d="M2 5 h13 c2 0 3 1 3 3 v19 c0-2-1-3-3-3 h-13 z M34 5 h-13 c-2 0-3 1-3 3 v19 c0-2 1-3 3-3 h13 z" fill="none" stroke="var(--brand-blue)" stroke-width="1.6" stroke-linejoin="round"/>
        </svg>
        Rick Fansome Crestwell Water &amp; Blaze Recovery LLC 5183 Tillcorn Rd Ashvale Cove, ST 00000
      </div>
      <div class="contact-row">
        <svg width="34" height="32" viewBox="0 0 34 32" aria-hidden="true">
          <rect x="6" y="3" width="22" height="16" rx="1.5" fill="none" stroke="var(--brand-blue)" stroke-width="1.6"/>
          <path d="M2 27 l4-6 h22 l4 6 z" fill="none" stroke="var(--brand-blue)" stroke-width="1.6" stroke-linejoin="round"/>
        </svg>
        rick@crestwellrecovery-example.com<br>www.crestwellrecovery-example.com
      </div>
    </div>
  </section>

</div>
</body>
</html>
```